Business Coaching Model and Flow Chart

We need this flowchart, attached, to be updated in a modern and engaging way. This flowchart is the cornerstone of a business coaching class we are running, and will be the main support reference for the people who take the class. We are open to ideas as to how it is presented, but we would like a largely minimalist look that leaves space to be impactful where the key information sites. Our colour scheme is primary red (D51C29), white, grey (333333), black, and secondary green (3C8740). We will also need our logo present (attached).

```html
<!DOCTYPE html>
<html lang="en">
<head>
<meta charset="UTF-8">
<title>Group to Teams Through Learning Together</title>
<link href="https://fonts.googleapis.com/css2?family=Fira+Sans:ital,wght@0,400;0,500;0,600;0,700;1,500;1,600&display=swap" rel="stylesheet">
<style>
  :root {
    --red: #d51c29;
    --white: #ffffff;
    --grey: #333333;
  }
  * { box-sizing: border-box; margin: 0; padding: 0; }
  html, body { width: 1200px; height: 675px; overflow: hidden; background: var(--white); }
  body { font-family: "Fira Sans", sans-serif; color: var(--grey); position: relative; }

  .brand { position: absolute; left: 18px; top: 18px; width: 90px; text-align: center; }
  .brand-mark { width: 78px; height: 78px; border-radius: 50%; background: var(--red); margin: 2px auto 6px; }
  .brand-name { font-size: 10px; font-weight: 700; color: var(--red); letter-spacing: .3px; text-transform: uppercase; }

  .title-band { position: absolute; left: 125px; top: 19px; right: 0; height: 94px; background: var(--red); padding: 13px 0 0 19px; }
  .title-band h1 { color: var(--white); font-size: 30px; font-weight: 700; line-height: 36px; letter-spacing: -.2px; }

  .stages { position: absolute; left: 0; top: 140px; width: 1200px; height: 96px; }
  .stage { position: absolute; top: 0; width: 95px; height: 95px; border-radius: 50%; border: 1.5px solid var(--red);
           display: flex; align-items: center; justify-content: center; text-align: center;
           color: var(--red); font-size: 11px; font-weight: 600; line-height: 13.5px; background: var(--white); }
  .stage-label { display: block; }
  .stage em { font-style: italic; font-weight: 500; }
  .stage.is-end { background: var(--red); color: var(--white); }
  .arrow { position: absolute; top: 38px; }

  .board { position: absolute; left: 52px; top: 250px; width: 1095px; height: 425px; display: flex; border-top: 1px solid var(--red); }
  .col { position: relative; height: 100%; border-right: 1px solid var(--red); padding-top: 30px; }
  .col:last-child { border-right: none; }
  .col.is-red { background: var(--red); color: var(--white); border-right: none; padding-top: 8px; }

  .problem { width: 157.5px; }
  .clarify { width: 155.6px; padding-left: 25px; }
  .plan { width: 156.4px; padding-left: 9px; }
  .learn { width: 156px; padding-left: 19px; }
  .doing { width: 156px; padding-left: 30px; }
  .reflect { width: 156.6px; padding-left: 9px; }
  .solution { width: 156.9px; }

  .item { font-size: 10.6px; font-weight: 500; line-height: 13px; height: 36px; }
  .item.tall { height: 50px; }
  .item.head { height: 19px; }
  .bullets { list-style: none; }
  .bullets li { font-size: 10.6px; font-weight: 400; line-height: 19px; position: relative; padding-left: 8px; }
  .bullets li::before { content: "•"; position: absolute; left: 0; }
  .bullets.after { margin-bottom: 24px; }

  .icon-list { list-style: none; }
  .icon-list li { height: 50px; display: flex; flex-direction: column; align-items: center; justify-content: flex-start;
                  font-size: 10.4px; font-weight: 500; line-height: 13px; text-align: center; }
  .icon-list svg { width: 20px; height: 20px; margin-bottom: 3px; flex: none; }
</style>
</head>
<body>

<div class="brand">
  <div class="brand-mark"></div>
  <div class="brand-name">Mara Ellison</div>
</div>

<header class="title-band">
  <h1>GROUP TO TEAMS<br>THROUGH LEARNING TOGETHER</h1>
</header>

<section class="stages">
  <div class="stage is-end" style="left:84px"><span class="stage-label">PROBLEM</span></div>
  <svg class="arrow" style="left:193px" width="34" height="20" viewBox="0 0 34 20"><path d="M0 10h28" stroke="#d51c29" stroke-width="2.5"/><path d="M24 2l9 8-9 8" fill="none" stroke="#d51c29" stroke-width="2.5"/></svg>
  <div class="stage" style="left:240px"><span class="stage-label">CLARIFY<br>CHALLENGES -<br>DIAGNOSTICS</span></div>
  <svg class="arrow" style="left:349px" width="34" height="20" viewBox="0 0 34 20"><path d="M0 10h28" stroke="#d51c29" stroke-width="2.5"/><path d="M24 2l9 8-9 8" fill="none" stroke="#d51c29" stroke-width="2.5"/></svg>
  <div class="stage" style="left:396px"><span class="stage-label">PLANNING<br>FOR SUCCESS<br><em>Make a Plan</em></span></div>
  <svg class="arrow" style="left:505px" width="34" height="20" viewBox="0 0 34 20"><path d="M0 10h28" stroke="#d51c29" stroke-width="2.5"/><path d="M24 2l9 8-9 8" fill="none" stroke="#d51c29" stroke-width="2.5"/></svg>
  <div class="stage" style="left:552px"><span class="stage-label">LEARN<br>THE TOOLS<br>Workshops</span></div>
  <svg class="arrow" style="left:661px" width="34" height="20" viewBox="0 0 34 20"><path d="M0 10h28" stroke="#d51c29" stroke-width="2.5"/><path d="M24 2l9 8-9 8" fill="none" stroke="#d51c29" stroke-width="2.5"/></svg>
  <div class="stage" style="left:708px"><span class="stage-label">DOING<br><em>Mastering<br>the Tools</em></span></div>
  <svg class="arrow" style="left:817px" width="34" height="20" viewBox="0 0 34 20"><path d="M0 10h28" stroke="#d51c29" stroke-width="2.5"/><path d="M24 2l9 8-9 8" fill="none" stroke="#d51c29" stroke-width="2.5"/></svg>
  <div class="stage" style="left:865px"><span class="stage-label">REFLECT<br>ADAPT<br>EMBED</span></div>
  <svg class="arrow" style="left:974px" width="34" height="20" viewBox="0 0 34 20"><path d="M0 10h28" stroke="#d51c29" stroke-width="2.5"/><path d="M24 2l9 8-9 8" fill="none" stroke="#d51c29" stroke-width="2.5"/></svg>
  <div class="stage is-end" style="left:1021px"><span class="stage-label">SOLUTION</span></div>
</section>

<main class="board">
  <div class="col is-red problem">
    <ul class="icon-list">
      <li><svg viewBox="0 0 20 20"><rect x="4" y="1" width="12" height="18" fill="#fff"/><path d="M7 12h6M7 15h6" stroke="#d51c29" stroke-width="1.2"/><path d="M10 4v5" stroke="#d51c29" stroke-width="1.2"/></svg>Underbilling</li>
      <li><svg viewBox="0 0 20 20" fill="#fff"><circle cx="5" cy="6" r="2.5"/><circle cx="15" cy="6" r="2.5"/><circle cx="10" cy="8" r="3"/><rect x="1" y="10" width="7" height="6" rx="2"/><rect x="12" y="10" width="7" height="6" rx="2"/><rect x="6" y="12" width="8" height="7" rx="2"/></svg>Staff Retention</li>
      <li><svg viewBox="0 0 20 20" fill="none" stroke="#fff" stroke-width="1.8"><circle cx="8" cy="8" r="6"/><path d="M12.5 12.5l6 6"/></svg>Hard to Recruit</li>
      <li><svg viewBox="0 0 20 20"><path d="M2 2h16v12h-6l-2 4-2-4H2z" fill="#fff"/><path d="M10 5v5M10 11.5v1.5" stroke="#d51c29" stroke-width="1.6"/></svg>Client Complaints</li>
      <li><svg viewBox="0 0 20 20"><circle cx="10" cy="10" r="8.5" fill="#fff"/></svg>Staff Stress &amp; Burnout</li>
      <li><svg viewBox="0 0 20 20" fill="none" stroke="#fff" stroke-width="1.4"><path d="M1 10h6M4 7l3 3-3 3M19 10h-6M16 7l-3 3 3 3M10 2l-2 8h4l-2 8"/></svg>Conflict</li>
      <li><svg viewBox="0 0 20 20" fill="none" stroke="#fff" stroke-width="1.6"><path d="M3 9a7 7 0 0 1 13-3M17 11a7 7 0 0 1-13 3"/><path d="M16 2v4h-4M4 18v-4h4"/></svg>Sector Constant Change</li>
      <li><svg viewBox="0 0 20 20"><path d="M4 1h12M4 19h12" stroke="#fff" stroke-width="2"/><path d="M5 2h10l-4 8 4 8H5l4-8z" fill="#fff"/></svg>Limited in Best Practice</li>
    </ul>
  </div>

  <div class="col clarify">
    <p class="item">Scoping</p>
    <p class="item">Interviews</p>
    <p class="item">Group Reflection</p>
    <p class="item">Opinion Surveys</p>
    <p class="item head">Certified Assessments</p>
    <ul class="bullets">
      <li>Personality Styles</li>
      <li>Work Preference</li>
      <li>Strengths &amp; Values</li>
      <li>Trust</li>
      <li>360</li>
    </ul>
  </div>

  <div class="col plan">
    <p class="item tall">Team Data Analysis<br>Workshop</p>
    <p class="item">Individual Development Plan</p>
    <p class="item">Team Development Plan</p>
    <p class="item">Organizational Plan</p>
  </div>

  <div class="col learn">
    <p class="item head">Foundation Workshops</p>
    <ul class="bullets after">
      <li>Difficult Conversations</li>
      <li>Giving &amp; Receiving<br>Feedback</li>
      <li>Values Alignment</li>
      <li>Shared Purpose</li>
      <li>Ways of Working</li>
      <li>Diversity</li>
      <li>Wellbeing</li>
      <li>Time Management</li>
    </ul>
    <p class="item">Customised Workshops</p>
  </div>

  <div class="col doing">
    <p class="item">Group Coaching</p>
    <p class="item">Team Coaching</p>
    <p class="item">Individual Coaching</p>
    <p class="item">Peer Learning</p>
    <p class="item">Lunch ’n Learn</p>
  </div>

  <div class="col reflect">
    <p class="item">Culture Committee</p>
    <p class="item">Embedding Workshop</p>
    <p class="item">Culture Collateral</p>
    <p class="item">WOW Manifesto</p>
    <p class="item">Leadership Team Coaching</p>
    <p class="item">Measure ROI</p>
    <p class="item">Review Success</p>
    <p class="item">Evaluation Surveys</p>
    <p class="item">Temperature Checks</p>
    <p class="item">Recruit to Suit</p>
    <p class="item">Future Proofing - What Next?</p>
  </div>

  <div class="col is-red solution">
    <ul class="icon-list">
      <li><svg viewBox="0 0 20 20" fill="#fff"><circle cx="10" cy="5" r="4"/><rect x="5" y="10" width="10" height="9" rx="3"/></svg>Self Awareness &amp; Ownership</li>
      <li><svg viewBox="0 0 20 20" fill="none" stroke="#fff" stroke-width="1.8"><path d="M2 9l5-5 4 3 3-3 4 5-7 7z"/></svg>Partnership</li>
      <li><svg viewBox="0 0 20 20" fill="#fff"><circle cx="5" cy="4" r="2"/><circle cx="10" cy="4" r="2"/><circle cx="15" cy="4" r="2"/><rect x="2" y="8" width="16" height="4"/><rect x="4" y="13" width="12" height="6"/></svg>Great Place to Work</li>
      <li><svg viewBox="0 0 20 20" fill="#fff"><path d="M10 2c3 3 3 7 0 10-3-3-3-7 0-10zM2 8c4 0 7 2 8 6-4 0-7-2-8-6zM18 8c-4 0-7 2-8 6 4 0 7-2 8-6z"/><rect x="6" y="15" width="8" height="4"/></svg>Growth Mindset</li>
      <li><svg viewBox="0 0 20 20" fill="#fff"><path d="M3 8h4l9-5v14l-9-5H3z"/><rect x="5" y="12" width="3" height="6"/></svg>Coach Approach Culture</li>
      <li><svg viewBox="0 0 20 20"><rect x="1" y="4" width="18" height="11" fill="#fff"/><path d="M9 15l1 3 1-3" fill="#fff"/><circle cx="5.5" cy="9.5" r="1.5" fill="#d51c29"/><circle cx="10" cy="9.5" r="1.5" fill="#d51c29"/><circle cx="14.5" cy="9.5" r="1.5" fill="#d51c29"/></svg>Feedback Culture</li>
      <li><svg viewBox="0 0 20 20" fill="none" stroke="#fff" stroke-width="1.8"><circle cx="8" cy="8" r="4"/><path d="M8 1v3M8 12v3M1 8h3M12 8h3M11 11l7 7"/></svg>Way to Manage Conflict</li>
      <li><svg viewBox="0 0 20 20" fill="#fff"><path d="M1 2h14v9H6l-3 3v-3H1z"/><path d="M16 6h3v9h-2v3l-3-3H8v-2h8z"/></svg>Best Practice<br>Communication Skills</li>
    </ul>
  </div>
</main>

</body>
</html>
```